Flyer Needed for Westland Advocacy Summit 2017

We need a flyer designed for a save the date for Verdant Goods Forum in California on August 23, 2017. The lobby day is taking place in Sacramento so please design the flyer using these details.

Requirements
Must have
• - Date must be clear
Nice to have
• - Must have "save the date"
• - Something that catches your eye

```html
<!DOCTYPE html>
<html lang="en">
<head>
<meta charset="utf-8">
<title>Verdant Goods Forum – Save the Date</title>
<link href="https://fonts.googleapis.com/css2?family=Kaushan+Script&family=Raleway:wght@300;400&display=swap" rel="stylesheet">
<style>
  :root {
    --leaf-pale: #e6edd6;
    --leaf-soft: #cfdcae;
    --leaf-mid: #a9c46a;
    --leaf-deep: #7f9c5a;
    --ribbon: #a8c666;
    --title-light: #c8d75c;
    --title-main: #a2c35c;
    --halo: rgba(255, 255, 255, 0.55);
    --city: #c7ab98;
    --white: #ffffff;
  }
  html, body {
    margin: 0;
    padding: 0;
    overflow: hidden;
    background: var(--leaf-pale);
  }
  .flyer {
    position: relative;
    width: 801px;
    height: 1200px;
    overflow: hidden;
    font-family: "Raleway", Arial, sans-serif;
  }
  .leaf-backdrop {
    position: absolute;
    inset: 0;
    background:
      radial-gradient(ellipse 260px 360px at 20% 8%, var(--leaf-soft), transparent 70%),
      radial-gradient(ellipse 220px 320px at 88% 22%, var(--leaf-soft), transparent 70%),
      radial-gradient(ellipse 240px 300px at 8% 80%, var(--leaf-mid), transparent 70%),
      radial-gradient(ellipse 260px 300px at 82% 88%, var(--leaf-soft), transparent 70%),
      radial-gradient(ellipse 200px 240px at 50% 98%, var(--leaf-mid), transparent 70%),
      linear-gradient(160deg, #e9efdc, var(--leaf-pale) 50%, #dfe8cb);
  }
  .halo {
    position: absolute;
    left: 81px;
    top: 244px;
    width: 640px;
    height: 640px;
    border-radius: 50%;
    background: var(--halo);
  }
  .ribbon {
    position: absolute;
    left: 283px;
    top: 309px;
    width: 235px;
    height: 40px;
    background: var(--ribbon);
    color: var(--white);
    font-size: 23px;
    font-weight: 300;
    letter-spacing: 2px;
    line-height: 40px;
    text-align: center;
  }
  .event-date {
    position: absolute;
    left: 283px;
    top: 358px;
    width: 235px;
    display: flex;
    align-items: center;
    gap: 8px;
    color: var(--ribbon);
    font-size: 16px;
    letter-spacing: 1.5px;
  }
  .event-date::before,
  .event-date::after {
    content: "";
    flex: 1;
    height: 2px;
    background: var(--ribbon);
  }
  .title {
    position: absolute;
    left: 0;
    right: 0;
    top: 380px;
    margin: 0;
    font-family: "Kaushan Script", cursive;
    font-weight: 400;
    text-align: center;
    line-height: 1;
  }
  .title span { display: block; }
  .title .word-one { font-size: 96px; color: var(--title-light); }
  .title .word-two { font-size: 124px; color: var(--title-main); margin-top: -6px; }
  .title .word-three { font-size: 96px; color: var(--title-light); margin-top: -4px; }
  .city {
    position: absolute;
    left: 0;
    right: 0;
    top: 795px;
    text-align: center;
    color: var(--city);
    font-size: 22px;
    font-weight: 300;
    letter-spacing: 3px;
  }
  .sprig {
    position: absolute;
    left: 356px;
    top: 840px;
    width: 82px;
    height: 16px;
  }
</style>
</head>
<body>
  <main class="flyer">
    <div class="leaf-backdrop" role="img" aria-label="Pattern of hand-drawn green and white leaves with scalloped and striped fills"></div>
    <div class="halo"></div>
    <div class="ribbon">save the date</div>
    <div class="event-date">08.23.2017</div>
    <h1 class="title">
      <span class="word-one">Verdant</span>
      <span class="word-two">Goods</span>
      <span class="word-three">Forum</span>
    </h1>
    <div class="city">SACRAMENTO</div>
    <svg class="sprig" viewBox="0 0 82 16" role="img" aria-label="Small green sprig ornament">
      <line x1="0" y1="8" x2="60" y2="8" stroke="#a8c666" stroke-width="2"/>
      <ellipse cx="70" cy="8" rx="10" ry="5" fill="#a8c666"/>
    </svg>
  </main>
</body>
</html>
```